WP website design (Harwick)

We need a wordpress design for an established auction and real estate company based in Florida. The winning design will incorporate a professional color scheme with company logo in a clean layout. The design needs to consider that this will be developed on a responsive theme. Colors are those that will highlight the logo.

Industry/Entity Type

Real Estate

Font styles to use
Serif
Sans Serif

Colors

Designer to choose colors to be used in the design.

Requirements
Must have
• Navigation:
1) Home
2) Auctions
3) Online Auctions
4) About Us
5) Services
6) Real Estate Listings
7) References
8) Contact Us

Colors will be blue (#000066) / red (#B10000) and black or other complementary color. Tagline to be used "Since 1977, Proven Results." Slideshow to be placed in the header or body of home page - please use stock real estate image.

Widgets: 1) Email Sign-up 2) Social media icons for FB and LinkedIn 3) Featured Listings 4) Testimonials 5) Register button

Footer will have smaller company logo, attached logos and contact info:
Phone: (555) 612-4408 Mobile: (555) 719-2263
Email: lorahartwick@mailvine.example
Address: 48 E. Marlow Avenue, Ste 317, Port Averly, AV 39815
Nice to have
• Use of a drop down menu:
Auctions-
1) Upcoming Auctions
2) Past Auctions

```html
<!DOCTYPE html>
<html lang="en">
<head>
<meta charset="utf-8">
<title>Harwick Auctions</title>
<link href="https://fonts.googleapis.com/css2?family=Source+Sans+3:ital,wght@0,400;0,600;0,700;1,400&family=Montserrat:wght@400&display=swap" rel="stylesheet">
<style>
:root{
  --navy:#22288f;
  --red:#c8101a;
  --red-deep:#b10000;
  --red-dark:#8e1014;
  --text:#222;
  --muted:#6d6d6d;
  --nav:#7a7a7a;
  --rule:#e4e4e4;
  --white:#fff;
}
*{margin:0;padding:0;box-sizing:border-box}
html,body{width:823px;height:1200px;overflow:hidden;background:var(--white)}
body{position:relative;font-family:"Source Sans 3",Arial,sans-serif;font-weight:400;color:var(--text)}
.abs{position:absolute}
a{color:inherit;text-decoration:none}
ul{list-style:none}

/* header */
.brand{left:77px;top:20px;display:flex;align-items:center;gap:10px}
.brand-mark{width:46px;height:46px;background:var(--navy)}
.brand-name{font-size:30px;font-weight:700;color:var(--navy);line-height:1}
.brand-sub{font-size:14px;font-weight:700;color:var(--navy);letter-spacing:8px;margin-top:4px}
.btn{display:inline-flex;align-items:center;justify-content:center;background:linear-gradient(#d91c22,#b10000);color:#fff;font-weight:700;border-radius:8px;font-size:9px}
.register{left:698px;top:38px;width:49px;height:27px}
.nav{top:85px;left:77px;width:670px;display:flex;justify-content:space-between;font-size:8px;font-weight:400;color:var(--nav);text-transform:uppercase}
.nav li{height:21px;display:flex;align-items:center;padding:0 6px}
.nav li.active{background:var(--red);color:#fff;border-radius:6px}
.dropdown{left:150px;top:117px;width:115px;height:52px;background:var(--red);border-radius:6px;color:#fff;font-size:8px;font-weight:400;text-transform:uppercase;padding:11px 12px;z-index:3}
.dropdown:before{content:"";position:absolute;left:17px;top:-6px;border:6px solid transparent;border-top:0;border-bottom-color:var(--red)}
.dropdown li{display:flex;align-items:center;gap:6px;margin-bottom:7px}
.dropdown li:before{content:"";border-left:6px solid #fff;border-top:4px solid transparent;border-bottom:4px solid transparent}

/* hero */
.hero-band{left:0;top:115px;width:823px;height:239px;background:linear-gradient(90deg,#9c0007,#e3171c 40%,#c50a10 70%,#e0151a)}
.hero-photo{left:77px;top:115px;width:670px;height:239px;background:linear-gradient(160deg,#5f5a52 0%,#b6aea2 35%,#8b7a66 60%,#4a3a2c 100%)}
.tagline-box{left:77px;top:212px;width:271px;height:58px;background:rgba(40,40,40,.35)}
.tagline{left:96px;top:231px;font-family:"Montserrat",sans-serif;font-size:16px;color:#fff}
.dots{left:397px;top:337px;display:flex;gap:6px}
.dots span{width:6px;height:6px;border-radius:50%;background:#ddd}
.dots span.on{background:var(--red)}
.fade{left:0;top:354px;width:823px;height:36px;background:linear-gradient(#d8d8d8,#fff)}

/* content */
h2{font-size:14px;font-weight:400;color:#111;text-transform:uppercase;letter-spacing:.2px}
h2 em{font-style:normal;font-weight:700;color:var(--red-deep)}
.welcome{left:77px;top:397px;width:440px}
.welcome .lead{font-size:8px;font-weight:400;font-style:italic;color:#333;margin-top:4px;text-transform:uppercase}
.welcome p{font-size:8px;line-height:1.3;color:var(--muted);margin-top:17px}
.welcome p+p{margin-top:14px}
.read-more{left:77px;top:524px;width:57px;height:26px}
.news{left:535px;top:390px;width:212px}
.news-item{display:flex;gap:6px;margin-top:11px}
.news-item+.news-item{margin-top:16px}
.thumb{width:58px;height:42px;background:linear-gradient(#5d7fb4,#b9c3cc 60%,#7a7a70)}
.news-date{font-size:7px;color:#aaa}
.news-title{font-size:8px;color:#111;margin-top:4px}
.news-more{font-size:7.5px;color:var(--red-deep);margin-top:18px}
.divider{left:77px;top:569px;width:670px;height:1px;background:var(--rule)}
.col{top:590px;width:212px}
.col .sub{font-size:8.6px;color:var(--navy);margin-top:4px}
.col-sep{top:590px;width:1px;height:230px;background:var(--rule)}
.listing-photo{left:77px;top:641px;width:211px;height:138px;background:linear-gradient(#3f6eb8,#88a8d2 30%,#b98f62 55%,#7b6a50)}
.chev{left:278px;top:612px}
.services{margin-top:19px}
.services li{font-size:8.3px;color:#333;margin-top:3.5px;display:flex;align-items:center;gap:5px}
.services li:before{content:"";width:4px;height:4px;border-right:1px solid #333;border-top:1px solid #333;transform:rotate(45deg)}
.quote{font-size:8.3px;line-height:1.6;color:#444;margin-top:14px}
.author{font-size:8px;font-style:italic;color:var(--red-deep);margin-top:14px}
.role{font-size:8px;font-style:italic;color:#111;margin-top:3px}
.next{left:535px;top:727px;width:19px;height:19px;border-radius:50%;background:#e6e6e6}
.view{top:788px;width:58px;height:27px}

/* footer */
.footer{left:0;top:861px;width:823px;height:301px;background:linear-gradient(#d9242a,#b50a0f)}
.fcol{top:881px;color:#fff}
.fcol h3{font-size:9.8px;font-weight:700;text-transform:uppercase;line-height:1.1}
.fnote{left:421px;top:892px;font-size:8.5px;font-weight:400;color:#fff}
.frule{top:907px;height:1px;background:rgba(255,255,255,.35)}
.fcol li{font-size:8.6px;font-weight:400;color:#fff;line-height:14px}
.email-field{left:421px;top:923px;width:132px;height:35px;background:#fff;font-size:8.3px;color:#aaa;padding:12px 9px}
.subscribe{left:421px;top:977px;width:65px;height:22px;border-radius:11px;background:linear-gradient(#444,#111);color:#fff;font-size:8.6px;font-weight:600;display:flex;align-items:center;justify-content:center}
.social{left:704px;top:912px;display:flex;gap:2px}
.social span{width:20px;height:20px;border-radius:50%;background:#fff}
.partners{left:139px;top:1095px;width:545px;height:57px;background:#fff;border-radius:6px;display:flex;align-items:center;justify-content:space-around;padding:0 14px}
.partners span{background:#d6dbe4;border-radius:3px;height:24px}
.bottom{left:0;top:1162px;width:823px;height:38px;background:var(--red-dark);color:#f2d6d6;font-size:7.5px;display:flex;align-items:center;justify-content:center}
</style>
</head>
<body>

<header>
  <div class="abs brand">
    <span class="brand-mark"></span>
    <div>
      <div class="brand-name">Harwick</div>
      <div class="brand-sub">AUCTIONS</div>
    </div>
  </div>
  <a class="abs btn register" href="#">Register</a>
  <ul class="abs nav">
    <li>Home</li><li class="active">Auctions</li><li>Online Auctions</li><li>About Us</li><li>Services</li><li>Real Estate Listings</li><li>References</li><li>Contact Us</li>
  </ul>
  <ul class="abs dropdown">
    <li>Upcoming Auctions</li>
    <li>Past Auctions</li>
  </ul>
</header>

<section>
  <div class="abs hero-band"></div>
  <div class="abs hero-photo" role="img" aria-label="Modern kitchen interior with wooden counter and large windows onto a forest"></div>
  <div class="abs tagline-box"></div>
  <div class="abs tagline">SINCE 1977, PROVEN RESULTS</div>
  <div class="abs dots"><span></span><span class="on"></span><span class="on"></span></div>
  <div class="abs fade"></div>
</section>

<main>
  <div class="abs welcome">
    <h2>Welcome <em>Marlow Keys</em></h2>
    <div class="lead">Neque porro quisquam est qui dolorem ipsum quia dolor sit amet</div>
    <p>Lorem Ipsum is simply dummy text of the printing and typesetting industry. Lorem Ipsum has been the industry's standard dummy text ever since the 1500s</p>
    <p>when an unknown printer took a galley of type and scrambled it to make a type specimen book. It has survived not only five centuries, but also the leap into electronic typesetting, remaining essentially unchanged. I</p>
  </div>
  <a class="abs btn read-more" href="#">Read More</a>

  <div class="abs news">
    <h2>Latest <em>News</em></h2>
    <div class="news-item">
      <div class="thumb" role="img" aria-label="House balcony under blue sky"></div>
      <div><div class="news-date">Jun 14 2014</div><div class="news-title">Neque porro quisquam est</div></div>
    </div>
    <div class="news-item">
      <div class="thumb" role="img" aria-label="House roof and gables"></div>
      <div><div class="news-date">Jun 14 2014</div><div class="news-title">Neque porro quisquam est</div></div>
    </div>
    <div class="news-more">View More...</div>
  </div>

  <div class="abs divider"></div>

  <div class="abs col" style="left:76px">
    <h2>Featured <em>Listings</em></h2>
    <div class="sub">Please visit the General Property auction site</div>
  </div>
  <svg class="abs chev" width="10" height="12" viewBox="0 0 10 12"><path d="M2 1l5 5-5 5" fill="none" stroke="#ccc" stroke-width="2"/></svg>
  <div class="abs listing-photo" role="img" aria-label="Adobe style house with wooden fence and desert plants"></div>
  <a class="abs btn view" style="left:77px" href="#">view More</a>

  <div class="abs col-sep" style="left:297px"></div>
  <div class="abs col" style="left:305px">
    <h2>Our <em>Services</em></h2>
    <div class="sub">Auctions are free and open to the public.</div>
    <ul class="services">
      <li>Auctions</li><li>Online Auctions</li><li>Upcoming Auctions</li><li>Past Auctions</li><li>Real Estate Listings</li><li>Contact Us</li>
    </ul>
  </div>
  <a class="abs btn view" style="left:306px" href="#">view More</a>

  <div class="abs col-sep" style="left:526px"></div>
  <div class="abs col" style="left:534px">
    <h2>Clients <em>Testimonials</em></h2>
    <div class="sub">Some of Our Clients talk about our Service</div>
    <p class="quote">"Neque porro quisquam est qui dolorem ipsum quia dolor sit amet, consectetur, adipisci velit..."</p>
    <div class="author">John Doe</div>
    <div class="role">Founder of Company</div>
  </div>
  <svg class="abs next" width="19" height="19" viewBox="0 0 19 19"><path d="M8 6l4 3.5-4 3.5" fill="none" stroke="#fff" stroke-width="1.5"/></svg>
  <a class="abs btn view" style="left:535px" href="#">view More</a>
</main>

<footer>
  <div class="abs footer"></div>
  <div class="abs fcol" style="left:77px;width:160px">
    <h3>Contact Us</h3>
    <ul style="margin-top:34px">
      <li>Phone: (555) 612-4408</li>
      <li>Mobile: (555) 719-2263</li>
      <li>Email: lorahartwick@mailvine.example</li>
      <li>Address: 48 E. Marlow Avenue, Ste 317,</li>
      <li>Port Averly, AV 39815</li>
    </ul>
  </div>
  <div class="abs frule" style="left:77px;width:154px"></div>
  <div class="abs fcol" style="left:249px;width:153px">
    <h3>Quick Links</h3>
    <ul style="margin-top:34px">
      <li>Home</li><li>Auctions</li><li>Online Auctions</li><li>About Us</li><li>Services</li><li>Real Estate Listings</li><li>References</li><li>Contact Us</li>
    </ul>
  </div>
  <div class="abs frule" style="left:249px;width:153px"></div>
  <div class="abs fcol" style="left:421px;width:153px">
    <h3>Subcribe our news letter</h3>
  </div>
  <div class="abs fnote">Get monthly our update to your mail</div>
  <div class="abs frule" style="left:421px;width:153px"></div>
  <div class="abs email-field">Enter your mail ID</div>
  <div class="abs subscribe">Subscribe</div>
  <div class="abs fcol" style="left:592px;width:155px;text-align:right">
    <h3>Get connect with us</h3>
  </div>
  <div class="abs frule" style="left:592px;width:155px"></div>
  <div class="abs social" aria-label="Social media links"><span></span><span></span></div>

  <div class="abs partners" aria-label="Partner associations">
    <span style="width:90px"></span>
    <span style="width:56px"></span>
    <span style="width:96px;height:36px"></span>
    <span style="width:126px;height:34px"></span>
    <span style="width:66px;height:30px"></span>
  </div>
  <div class="abs bottom">© 2014 Harwick. All rights reserved.</div>
</footer>

</body>
</html>
```